New name flyer

We have just changed our business name from kR Property group to Harbour Lantern. We want to distribute a flyer to the local community to inform them of the change. We are a realestate agency which focuses mainly on property management but also sales. We service from Brisbane to the Sunshine coast.

Target Market(s)

Local community

Industry/Entity Type

realestate

Requirements
Must have
• Details of name change
Nice to have
• Servicing area Brisbane and Sunshine Coast, no change in management or services we offer, and will continue pride ourselves on offering a high level of service, with the same team from the Gold to Sunshine Coast.
Should not have
• too much wording.

```html
<!DOCTYPE html>
<html lang="en">
<head>
<meta charset="utf-8">
<title>Harbour Lantern – New Name Flyer</title>
<link href="https://fonts.googleapis.com/css2?family=Montserrat:wght@400;500;600;700;800&display=swap" rel="stylesheet">
<style>
  :root {
    --board-blue: #33528a;
    --navy: #1f2a4a;
    --night: #1b1d2b;
    --gold: #e2bc4c;
    --gold-deep: #b47f31;
    --white: #ffffff;
    --sky-top: #6fa6d6;
    --sky-low: #d9c9a6;
    --city: #9a7a55;
    --water: #3d5f8a;
  }
  * { margin: 0; padding: 0; box-sizing: border-box; }
  html, body { width: 1200px; height: 849px; overflow: hidden; }
  body {
    background: var(--board-blue);
    font-family: "Montserrat", Arial, sans-serif;
    position: relative;
  }
  .board-name {
    position: absolute;
    left: 0; width: 1200px; top: 72px;
    text-align: center;
    color: var(--white);
    font-weight: 600;
    font-size: 22px;
    letter-spacing: 1px;
  }
  .flyer {
    position: absolute;
    left: 182px; top: 170px;
    width: 836px; height: 588px;
    background: var(--night);
    overflow: hidden;
  }
  .photo {
    position: absolute; top: 0; height: 304px;
    background: linear-gradient(180deg, var(--sky-top) 0%, var(--sky-low) 45%, var(--city) 72%, var(--water) 88%, #25406a 100%);
  }
  .photo--left { left: 0; width: 116px;
    background: linear-gradient(180deg, var(--sky-top) 0%, var(--sky-low) 35%, var(--city) 60%, #4f5a35 100%); }
  .photo--right { left: 420px; width: 416px; }
  .band-white { position: absolute; left: 0; width: 836px; top: 310px; height: 19px; background: linear-gradient(180deg, #ffffff, #e6e6e6); }
  .band-gold { position: absolute; left: 0; width: 836px; top: 336px; height: 8px; background: var(--gold); }
  .column {
    position: absolute; left: 116px; top: 0; width: 304px; height: 588px;
    background: linear-gradient(180deg, var(--gold) 0%, #d3a540 45%, var(--gold-deep) 100%);
    box-shadow: 0 0 8px rgba(0,0,0,0.35);
  }
  .column__head {
    height: 167px; background: var(--white);
    display: flex; align-items: center; padding-left: 28px;
  }
  .column__name { color: var(--navy); font-weight: 600; font-size: 22px; letter-spacing: 0.5px; }
  .slogan {
    position: absolute; left: 27px; top: 218px;
    color: var(--navy); font-weight: 800; font-size: 25px;
    line-height: 25px; letter-spacing: -1.3px;
  }
  .old-name {
    position: absolute; left: 27px; top: 279px;
    color: var(--white); font-weight: 600; font-size: 16.5px; letter-spacing: 2.4px;
  }
  .changing {
    position: absolute; left: 28px; top: 308px;
    color: var(--navy); font-weight: 600; font-size: 12.5px; letter-spacing: 2px;
  }
  .new-name {
    position: absolute; left: 27px; top: 420px; width: 260px;
    color: var(--white); font-weight: 600; font-size: 34px; line-height: 40px; letter-spacing: 0.5px;
  }
  .message { position: absolute; left: 437px; top: 383px; width: 399px; }
  .message__title {
    color: var(--gold); font-weight: 800; font-size: 18.5px;
    line-height: 22px; letter-spacing: -0.6px;
  }
  .message__rule { height: 2px; background: var(--gold); margin: 12px 0 12px 0; }
  .message__body { color: var(--white); font-size: 13.5px; line-height: 16.2px; letter-spacing: -0.3px; }
</style>
</head>
<body>
  <div class="board-name">HARBOUR LANTERN</div>

  <section class="flyer">
    <div class="photo photo--left" role="img" aria-label="City high-rise towers and trees at sunset"></div>
    <div class="photo photo--right" role="img" aria-label="City skyline across the river at golden hour"></div>
    <div class="band-white"></div>
    <div class="band-gold"></div>

    <div class="column">
      <div class="column__head"><span class="column__name">HARBOUR LANTERN</span></div>
      <h1 class="slogan">OUT WITH THE OLD,<br>IN WITH THE NEW.</h1>
      <p class="old-name">KR PROPERTY GROUP</p>
      <p class="changing">IS CHANGING IT’S NAME TO</p>
      <p class="new-name">HARBOUR LANTERN</p>
    </div>

    <div class="message">
      <h2 class="message__title">THE SAME PROPERTY COMPANY<br>YOU’VE ALWAYS TRUSTED.</h2>
      <div class="message__rule"></div>
      <p class="message__body">We are still the same team.<br>No change in management or services.<br>And we continue to pride ourselves in offering<br>high levels of services from the Gold to<br>Sunshine Coast.</p>
    </div>
  </section>
</body>
</html>
```